QRV MOONLIT GLOW Party

Hi,
Want to design a flyer for a party.

I have attached a design I would like you to work from and just add in the correct text:

QRV Events presents

November 2013

MOONLIT GLOW
PARTY

DJ COPPER LANTERN
VENUE: TBA

DOORS OPEN 8PM

ENTRY STRICTLY OVER 18'S.

DRESS CODE: SMART CASUAL SULTRY SEXY SPRING THREADS

COST: $60 PER HEAD, includes champagne, beer & wine and canapes.

Tickets from www.quietrivervista.com.au or 0491 570 156.

```html
<!DOCTYPE html>
<html lang="en">
<head>
<meta charset="utf-8">
<title>QRV Moonlit Glow Party – Flyer</title>
<link rel="stylesheet" href="https://fonts.googleapis.com/css2?family=Black+Ops+One&family=Josefin+Sans:wght@300;400;600&family=UnifrakturCook:wght@700&display=swap">
<style>
  :root {
    --page: #2b2b2d;
    --flyer-dark: #161113;
    --flyer-mid: #2c2428;
    --frame: rgba(235, 225, 230, 0.55);
    --ribbon: #3a3234;
    --ribbon-edge: #5a5052;
    --text-light: #f3eef2;
    --text-soft: #d9d1d6;
    --date-ink: #2a2336;
    --disc: #e9e4f2;
    --disc-edge: #b9b0cc;
    --banner: #8e2a1c;
    --banner-edge: #c9532e;
    --title-orange: #f49a3a;
    --title-glow: #ffcf7a;
    --club-purple: #6a1f6e;
    --club-glow: #e07be6;
    --speaker-warm: #e8a08a;
    --speaker-violet: #8a6fb8;
    --cloud: #e6e2ec;
  }
  * { box-sizing: border-box; margin: 0; padding: 0; }
  html, body { width: 1200px; height: 1000px; overflow: hidden; }
  body {
    background: var(--page);
    font-family: "Josefin Sans", sans-serif;
    color: var(--text-light);
    position: relative;
  }
  .flyer {
    position: absolute;
    left: 290px; top: 47px;
    width: 620px; height: 905px;
    background: var(--flyer-dark);
    overflow: hidden;
    box-shadow: 0 0 0 1px #000;
  }
  .flyer-frame {
    position: absolute; inset: 8px;
    border: 1px solid var(--frame);
    pointer-events: none;
    z-index: 20;
  }
  .backdrop {
    position: absolute; inset: 0;
    background: linear-gradient(180deg, #3a2e3c 0%, var(--flyer-mid) 35%, var(--flyer-dark) 70%, #0f0b0c 100%);
  }
  .model-photo {
    position: absolute;
    left: 200px; top: 9px;
    width: 240px; height: 360px;
    background: linear-gradient(180deg, #5a4650 0%, #9a7c80 45%, #6a5060 100%);
  }
  .speaker-area {
    position: absolute;
    border-radius: 50%;
    background: radial-gradient(circle, var(--speaker-warm) 0%, var(--speaker-violet) 100%);
  }
  .speaker-left { left: 12px; top: 222px; width: 196px; height: 196px; }
  .speaker-right { left: 420px; top: 250px; width: 182px; height: 182px; }
  .cloud-area {
    position: absolute;
    left: 9px; top: 470px;
    width: 602px; height: 110px;
    background: linear-gradient(180deg, rgba(230, 226, 236, 0) 0%, rgba(230, 226, 236, 0.45) 50%, rgba(230, 226, 236, 0) 100%);
  }
  .presents-ribbon {
    position: absolute;
    left: 0; top: 62px;
    width: 206px; height: 34px;
    background: linear-gradient(180deg, var(--ribbon-edge), var(--ribbon));
    clip-path: polygon(0 0, 100% 0, 92% 50%, 100% 100%, 0 100%);
    font-size: 17px; font-weight: 400;
    line-height: 36px;
    padding-left: 20px;
    color: var(--text-light);
    z-index: 5;
  }
  .date-disc {
    position: absolute;
    left: 189px; top: 346px;
    width: 236px; height: 236px;
    border-radius: 50%;
    background: radial-gradient(circle at 50% 40%, #ffffff 0%, var(--disc) 60%, var(--disc-edge) 100%);
    box-shadow: 0 0 0 6px rgba(255, 255, 255, 0.6), 0 0 0 9px rgba(140, 120, 170, 0.7);
    font-family: "Black Ops One", sans-serif;
    color: var(--date-ink);
    z-index: 4;
  }
  .date-day { position: absolute; left: 0; right: 0; top: 72px; text-align: center; font-size: 36px; letter-spacing: 1px; }
  .date-month { position: absolute; left: 36px; top: 114px; font-size: 32px; }
  .date-year { position: absolute; left: 0; right: 0; top: 152px; text-align: center; font-size: 44px; letter-spacing: 2px; }
  .title-banner {
    position: absolute;
    left: 39px; top: 566px;
    width: 536px; height: 54px;
    background: linear-gradient(180deg, var(--banner-edge), var(--banner));
    border: 2px solid #e8b58a;
    text-align: center;
    z-index: 6;
  }
  .title-text {
    font-family: "UnifrakturCook", serif;
    font-weight: 700;
    font-size: 38px;
    line-height: 50px;
    color: var(--title-orange);
    text-shadow: 0 0 8px var(--title-glow), 1px 1px 0 #5a1a10;
    letter-spacing: 1px;
    white-space: nowrap;
  }
  .rule { position: absolute; height: 1px; background: rgba(255, 255, 255, 0.45); z-index: 6; }
  .rule-top { top: 632px; left: 110px; width: 400px; }
  .rule-mid { top: 688px; left: 120px; width: 380px; }
  .dj-name {
    position: absolute;
    left: 0; right: 0; top: 644px;
    text-align: center;
    font-size: 30px; font-weight: 300;
    line-height: 36px;
    letter-spacing: 1px;
    z-index: 6;
  }
  .details-left {
    position: absolute;
    left: 80px; top: 698px;
    width: 210px;
    text-align: center;
    font-weight: 300;
    z-index: 6;
  }
  .details-left .line { font-size: 15px; line-height: 20px; text-transform: uppercase; }
  .details-left .venue { font-size: 18px; line-height: 22px; }
  .details-left .price { font-size: 27px; font-weight: 400; line-height: 34px; }
  .details-left .includes { font-size: 13px; line-height: 18px; padding-left: 24px; }
  .divider { position: absolute; left: 296px; top: 700px; width: 2px; height: 138px; background: var(--text-soft); z-index: 6; }
  .details-right {
    position: absolute;
    left: 314px; top: 696px;
    width: 290px;
    font-weight: 300;
    z-index: 6;
  }
  .details-right .guest { font-size: 24px; line-height: 30px; }
  .details-right .guest strong { font-weight: 600; }
  .details-right .dress { font-size: 15px; margin-top: 6px; padding-left: 10px; }
  .details-right .small-caps { font-size: 13px; text-transform: uppercase; }
  .details-right .threads { font-size: 13px; text-align: right; margin-top: 10px; padding-right: 18px; }
  .details-right .info { font-size: 19px; margin-top: 6px; }
  .details-right .tickets { font-size: 13px; margin-top: 4px; }
  .club-name {
    position: absolute;
    left: 0; right: 0; top: 852px;
    text-align: center;
    font-family: "Black Ops One", sans-serif;
    font-size: 34px;
    line-height: 40px;
    color: var(--club-purple);
    text-shadow: 0 0 2px var(--club-glow), 0 0 6px var(--club-glow);
    letter-spacing: 1px;
    z-index: 6;
  }
</style>
</head>
<body>
  <main class="flyer">
    <div class="backdrop" role="img" aria-label="Dark lattice pattern background with violet light"></div>
    <div class="model-photo" role="img" aria-label="Photo of a party guest"></div>
    <div class="speaker-area speaker-left" role="img" aria-label="Loudspeaker illustration"></div>
    <div class="speaker-area speaker-right" role="img" aria-label="Loudspeaker illustration"></div>
    <div class="cloud-area" role="img" aria-label="Smoke cloud illustration"></div>

    <div class="presents-ribbon">QRV Events presents</div>

    <div class="date-disc">
      <span class="date-day">FRIDAY</span>
      <span class="date-month">17NOV</span>
      <span class="date-year">2013</span>
    </div>

    <div class="title-banner"><h1 class="title-text">MOONLIT GLOW PARTY</h1></div>

    <div class="rule rule-top"></div>
    <h2 class="dj-name">DJ COPPER LANTERN</h2>
    <div class="rule rule-mid"></div>

    <section class="details-left">
      <p class="line venue">Venue : TBA</p>
      <p class="line">Doors open 8pm</p>
      <p class="line">Entry strictly over 18s.</p>
      <p class="line price">$60 PER HEAD</p>
      <p class="includes">includes champagne, beer &amp;<br>wine and canapes.</p>
    </section>

    <div class="divider"></div>

    <section class="details-right">
      <p class="guest"><strong>Special</strong> Guest Star</p>
      <p class="dress">Dress code: <span class="small-caps">smart casual sultry</span></p>
      <p class="threads">SEXY SPRING THREADS</p>
      <p class="info">Info/resa: 0491 570 156.</p>
      <p class="tickets">Tickets from www.quietrivervista.com.au</p>
    </section>

    <p class="club-name">NIGHT CLUB</p>
    <div class="flyer-frame"></div>
  </main>
</body>
</html>
```